Re Design of Business Cards

We a Technology & Telecommunications company, we supply computer repairs suppy and services to home and business's, we also a Telecommunications company as well and that we supply Internet, Mobile Voice and Data and Voice Lines to home and business as well we want to get our business cards re designed that stand out but also state what we can do and that we also come to you, there is 4 of us in the business so we all need same business card design but just different names and phone numbers on all.
Ive upload our Logo as well. and current looking business cards.

Our current business cards does not make me excited and or stand out, to dark and does not say what we do, we leave our business cards in letter boxes some times and in receptions of villages for retiress so the reception can hand out, few times now there asked what do you do, so thinking one side is our contact details and other is our services

I think I like to also put our address onto it as well, very simple as its also my home address but it be good to have it on there

48 Pellow St - Tarrin Bay NSW 2257

We should also have our business rego number which is a ABN

ABN: 37 904 516 283

this way we all covered and we look very Professional

We would like to make some Points, 1st of All we just found out we do not need out ABN on our Business Cards so we can Remove that please

we would like the address for the business to be on cards as well,

On the flip side of the Business Cards we would like to list some of our services as below

High-Speed Internet for Home & Business
Managed IT Services & Support
Network Setup & Optimization
VoIP & Mobile Voice Solutions
Wi-Fi Installation & Troubleshooting
Smart Home & Office Technology
Data Backup & Cybersecurity
Onsite Home and Or Business

```html
<!DOCTYPE html>
<html lang="en">
<head>
<meta charset="utf-8">
<title>Corvane Business Cards</title>
<link href="https://fonts.googleapis.com/css2?family=Lato:wght@400;700;900&family=Roboto+Condensed:wght@400&display=swap" rel="stylesheet">
<style>
  :root {
    --stage: #2a2b2c;
    --teal: #12353c;
    --orange: #d9571c;
    --orange-bright: #f26a22;
    --green: #1fae12;
    --white: #ffffff;
    --ink: #2a2a2a;
  }
  * { box-sizing: border-box; margin: 0; padding: 0; }
  html, body { width: 1200px; height: 694px; overflow: hidden; }
  body { background: var(--stage); position: relative; font-family: "Lato", sans-serif; }

  .card {
    position: absolute;
    top: 182px;
    width: 540px;
    height: 330px;
    border-radius: 22px;
    overflow: hidden;
  }
  .card--services { left: 40px; background: var(--teal); }
  .card--contact { left: 620px; background: var(--white); }

  .brand {
    display: flex;
    align-items: center;
    gap: 14px;
    font-family: "Lato", sans-serif;
    font-weight: 900;
    color: var(--orange);
    letter-spacing: 6px;
  }
  .brand__dot { border-radius: 50%; background: var(--green); flex: none; }

  .card--services .brand { position: absolute; top: 46px; left: 0; right: 0; justify-content: center; font-size: 44px; }
  .card--services .brand__dot { width: 30px; height: 30px; }

  .service-list {
    position: absolute;
    top: 138px;
    left: 0; right: 0;
    list-style: none;
    font-family: "Roboto Condensed", sans-serif;
    color: var(--white);
    font-size: 18px;
    line-height: 32px;
    text-align: center;
  }
  .service-list li { white-space: nowrap; }
  .service-list li span { margin: 0 5px; }
  .service-list li span::before {
    content: "";
    display: inline-block;
    width: 7px; height: 7px;
    border-radius: 50%;
    background: var(--orange-bright);
    margin-right: 7px;
    vertical-align: middle;
  }

  .card--contact .brand { position: absolute; top: 34px; left: 34px; font-size: 40px; }
  .card--contact .brand__dot { width: 24px; height: 24px; }

  .person { position: absolute; top: 104px; left: 34px; }
  .person__name { font-weight: 700; font-size: 28px; color: var(--orange); }
  .person__role { font-size: 17px; color: var(--ink); margin-top: 2px; }

  .contact-list { position: absolute; top: 172px; left: 34px; list-style: none; font-size: 16px; color: var(--ink); }
  .contact-list li { display: flex; align-items: center; gap: 10px; height: 24px; }
  .contact-list svg { width: 18px; height: 18px; flex: none; }
  .address { position: absolute; top: 258px; left: 62px; font-size: 16px; line-height: 20px; color: var(--ink); }

  .footer-band { position: absolute; left: 0; bottom: 0; width: 540px; height: 330px; pointer-events: none; }
</style>
</head>
<body>

<section class="card card--services">
  <div class="brand"><span class="brand__dot"></span>CORVANE</div>
  <ul class="service-list">
    <li><span>High-Speed Internet for Home &amp; Business</span></li>
    <li><span>Managed IT Services &amp; Support</span><span>Network Setup &amp; Optimization</span></li>
    <li><span>VoIP &amp; Mobile Voice Solutions</span><span>Wi-Fi Installation &amp; Troubleshooting</span></li>
    <li><span>Smart Home &amp; Office Technology</span><span>Data Backup &amp; Cybersecurity</span></li>
    <li><span>Onsite Home and Or Business</span></li>
  </ul>
</section>

<section class="card card--contact">
  <div class="brand"><span class="brand__dot"></span>CORVANE</div>

  <div class="person">
    <div class="person__name">Reid Tallon</div>
    <div class="person__role">Sales Consultant</div>
  </div>

  <ul class="contact-list">
    <li>
      <svg viewBox="0 0 24 24" aria-hidden="true"><path fill="var(--green)" d="M6.6 10.8a15 15 0 0 0 6.6 6.6l2.2-2.2c.3-.3.7-.4 1-.2 1.1.4 2.3.6 3.6.6.6 0 1 .4 1 1V20c0 .6-.4 1-1 1A17 17 0 0 1 3 4c0-.6.4-1 1-1h3.5c.6 0 1 .4 1 1 0 1.3.2 2.5.6 3.6.1.3 0 .7-.2 1z"/></svg>
      1800 417 903
    </li>
    <li>
      <svg viewBox="0 0 24 24" aria-hidden="true"><rect x="6" y="2" width="12" height="20" rx="2" fill="none" stroke="var(--green)" stroke-width="2"/><circle cx="12" cy="18" r="1.2" fill="var(--green)"/></svg>
      0412 586 390
    </li>
    <li>
      <svg viewBox="0 0 24 24" aria-hidden="true"><rect x="2" y="5" width="20" height="14" rx="1" fill="var(--green)"/><path d="M2 6l10 7 10-7" fill="none" stroke="var(--white)" stroke-width="1.6"/></svg>
      reid@corvane.com.au
    </li>
  </ul>

  <div class="address">48 Pellow St - Tarrin<br>Bay NSW 2257</div>

  <svg class="footer-band" viewBox="0 0 540 330" aria-hidden="true">
    <path d="M0 330 L0 322 L320 322 L338 296 L540 262 L540 330 Z" fill="var(--orange)"/>
    <path d="M0 316 L318 316 L322 308 L0 308 Z" fill="var(--green)"/>
  </svg>
</section>

</body>
</html>
```